Modern & Fresh Sumeray Book Cover

Need a creative e-book cover for my book.

Title: Get Sumeray Sorted
Subtitle: Learn How To Easily Choose & Enroll in the Perfect Coverage at the Perfect Time.

Target Market(s)

60-70 year olds in the United States

Font styles to use
Sans Serif

Colors
9bcb3c
33a6d7

Requirements
Must have
• Must look modern and fresh.
• Use our company colors www.BrovaMint.com

```html
<!DOCTYPE html>
<html lang="en">
<head>
<meta charset="utf-8">
<title>Get Sumeray Sorted – BrovaMint</title>
<link href="https://fonts.googleapis.com/css2?family=Poppins:wght@500;700;800&display=swap" rel="stylesheet">
<style>
  :root {
    --brand-green: #8ff000;
    --brand-blue: #4fd0f3;
    --ink: #111111;
    --paper: #ffffff;
  }
  html, body {
    margin: 0;
    padding: 0;
    overflow: hidden;
    background: var(--paper);
  }
  .cover {
    position: relative;
    width: 849px;
    height: 1200px;
    overflow: hidden;
    background: var(--paper);
    font-family: "Poppins", sans-serif;
  }
  .cover__shapes {
    position: absolute;
    inset: 0;
    width: 849px;
    height: 1200px;
  }
  .brand {
    position: absolute;
    left: 40px;
    top: 58px;
    display: flex;
    flex-direction: column;
  }
  .brand__row {
    display: flex;
    align-items: center;
    gap: 8px;
  }
  .brand__dot {
    width: 14px;
    height: 14px;
    border-radius: 50%;
    background: var(--ink);
  }
  .brand__name {
    font-weight: 700;
    font-size: 40px;
    line-height: 1;
    color: var(--ink);
    letter-spacing: 0.5px;
  }
  .brand__tagline {
    margin-top: 4px;
    margin-left: 22px;
    font-weight: 700;
    font-size: 6.5px;
    letter-spacing: 0.6px;
    color: var(--ink);
  }
  .title {
    position: absolute;
    left: 52px;
    top: 0;
    margin: 0;
    font-weight: 800;
    font-size: 126px;
    line-height: 1;
    letter-spacing: 1px;
  }
  .title__line {
    position: absolute;
    left: 0;
    white-space: nowrap;
    text-shadow: 4px 6px 10px rgba(0, 0, 0, 0.18);
  }
  .title__line--blue { color: var(--brand-blue); }
  .title__line--green { color: var(--brand-green); }
  .title__line--one { top: 340px; }
  .title__line--two { top: 489px; }
  .title__line--three { top: 625px; }
  .subtitle {
    position: absolute;
    left: 54px;
    top: 787px;
    margin: 0;
    font-weight: 500;
    font-size: 18.5px;
    color: var(--ink);
    white-space: nowrap;
  }
</style>
</head>
<body>
<main class="cover">
  <svg class="cover__shapes" viewBox="0 0 596 842" preserveAspectRatio="none" aria-hidden="true">
    <defs>
      <filter id="soft-shadow" x="-10%" y="-10%" width="130%" height="130%">
        <feDropShadow dx="0" dy="3" stdDeviation="4" flood-color="#000" flood-opacity="0.25"/>
      </filter>
    </defs>
    <polygon class="shape-top-blue" points="250,0 596,0 596,242 188,80" fill="var(--brand-blue)"/>
    <polygon class="shape-top-green" points="0,0 416,0 0,148" fill="var(--brand-green)" filter="url(#soft-shadow)"/>
    <polygon class="shape-bottom-blue" points="0,614 420,768 160,842 0,842" fill="var(--brand-blue)"/>
    <polygon class="shape-bottom-green" points="596,700 596,842 150,842 420,768" fill="var(--brand-green)" filter="url(#soft-shadow)"/>
  </svg>

  <div class="brand">
    <div class="brand__row">
      <span class="brand__dot"></span>
      <span class="brand__name">BrovaMint</span>
    </div>
    <span class="brand__tagline">HEALTH PLAN GUIDES FOR YOU</span>
  </div>

  <h1 class="title">
    <span class="title__line title__line--blue title__line--one">GET</span>
    <span class="title__line title__line--green title__line--two">SUMERAY</span>
    <span class="title__line title__line--blue title__line--three">SORTED</span>
  </h1>

  <p class="subtitle">Learn How To Easily Choose &amp; Enroll in the Perfect Coverage at the Perfect Time</p>
</main>
</body>
</html>
```